Business Card and Presentation Folder for Roofing Company
Business Card and Presentation Folder for Roofing Company - Construction
Creative Brief
Professional
Mark Ellis
Field Supervisor
2718 Brennan Ave Suite 310 Kirkwood, MO 63122
855-555-SEAL
mellis@slatepeak.example
www.SlatePeakRestoration.example
IL License #207.538142
stay with our colors of Yellow PMS 106, Black, and White
we want Logo Residential & Commercial 314-555-0178 Accredited Member of the QCA with an A+ Rating possible tag line: Everything you need under One Roof! or: Dedicated to being the most Trusted name in the Roofing Industry!
WendySlatePeak WendySlatePeak
COMBINE #217 AND #208 AND I WILL FINALIZE
#216...PLEASE MAKE THE CHANGES I REQUESTED SO I CAN FINALIZE THIS......
I extended the context
I uploaded an example of what I want our 2 presentation folders to look like: commercial folder: the 9 ICONS WILL BE: Flat roof Industrial building, Factory, City Highrise building, Apartment (3 story), Church, Gas Station, Restaurant, Hotel, & Bank Residential Folder: 9 ICONS WILL BE: House, House with flat roof, Condo, Siding, Gutters, Insulation, Ventilation, Storm Damage, Water&Fire Damage (together)
I uploaded our logos. Our colors are Yellow PMS106, Black, and White.....please use only these colors. Need business cards and Presentation Folder 9x12" (standard size) I will need the final files in Photoshop PSD file with all layers visible so I can make any future changes myself. Thanks Wendy

```html
<!DOCTYPE html>
<html lang="en">
<head>
<meta charset="utf-8">
<title>Slate Peak Restoration – Business Card and Presentation Folder</title>
<link href="https://fonts.googleapis.com/css2?family=Tinos:wght@400;700&display=swap" rel="stylesheet">
<style>
  :root {
    --yellow: #fee300;
    --black: #111111;
    --white: #ffffff;
    --bg: #d9d9d9;
    --pocket: #2a2a2a;
  }
  * { box-sizing: border-box; margin: 0; padding: 0; }
  html, body { width: 1200px; height: 1049px; overflow: hidden; }
  body {
    background: var(--bg);
    font-family: "Tinos", "Times New Roman", serif;
    color: var(--black);
    position: relative;
  }
  .cards-strip {
    position: absolute; left: 0; top: 0; width: 1200px; height: 272px;
    background: #d0d0d0;
  }
  .folder-stage {
    position: absolute; left: 0; top: 284px; width: 1200px; height: 765px;
    background: linear-gradient(180deg, #cfcfcf, #e4e4e4);
  }
  .card {
    position: absolute; width: 448px; height: 252px; border-radius: 16px;
    background: var(--yellow); overflow: hidden;
  }
  .card--front { left: 134px; top: 12px; }
  .card--back { left: 610px; top: 12px; }

  .card__name { position: absolute; left: 26px; top: 66px; font-size: 29px; font-weight: 400; }
  .card__title { position: absolute; left: 28px; top: 106px; font-size: 17px; }
  .contact-list { position: absolute; left: 214px; top: 20px; list-style: none; font-size: 11.5px; line-height: 20.5px; }
  .contact-list li { display: flex; align-items: center; gap: 8px; }
  .contact-list li.wrap { line-height: 13px; align-items: flex-start; margin-top: 3px; }
  .contact-list .dot { width: 11px; height: 11px; border-radius: 50%; background: var(--black); flex: none; margin-top: 1px; }
  .card__band {
    position: absolute; left: 0; bottom: 16px; width: 100%; height: 28px; background: var(--black);
    display: flex; align-items: center; justify-content: space-between; padding: 0 14px 0 28px;
  }
  .card__license { color: var(--yellow); font-size: 11px; }

  .brand {
    display: flex; align-items: center; justify-content: center; gap: 10px;
    font-family: "Tinos", "Times New Roman", serif; font-weight: 700; line-height: 1;
    color: var(--black);
  }
  .brand__square { width: 0.6em; height: 0.6em; background: currentColor; flex: none; }
  .brand--small { font-size: 14px; color: var(--yellow); gap: 6px; }

  .card--back .brand { position: absolute; left: 0; top: 62px; width: 100%; font-size: 34px; }
  .card__statement {
    position: absolute; left: 0; top: 150px; width: 100%; height: 58px; background: var(--black);
    color: var(--white); text-align: center; font-size: 15px; line-height: 24px; padding-top: 5px;
  }
  .card__tagline { position: absolute; left: 0; top: 218px; width: 100%; text-align: center; font-size: 11.5px; }

  .folder-front {
    position: absolute; left: 70px; top: 140px; width: 345px; height: 460px; background: var(--black);
    box-shadow: 0 8px 24px rgba(0,0,0,.25);
  }
  .folder-front .brand--large { position: absolute; left: 0; top: 150px; width: 100%; font-size: 27px; color: var(--yellow); }
  .folder-front .brand--small { position: absolute; right: 16px; bottom: 50px; font-size: 13px; }
  .folder-front__stripes { position: absolute; left: 0; bottom: 24px; width: 100%; }
  .folder-front__stripes span { display: block; height: 6px; background: var(--yellow); margin-top: 5px; }
  .folder-front__stripes span:first-child { width: 100%; height: 8px; }
  .folder-front__stripes span:last-child { width: 72%; }

  .folder-inside {
    position: absolute; left: 470px; top: 140px; width: 660px; height: 460px; background: var(--white);
    box-shadow: 0 8px 24px rgba(0,0,0,.2); display: flex;
  }
  .folder-inside__panel { flex: 1; position: relative; }
  .folder-inside__panel + .folder-inside__panel { border-left: 1px solid #e2e2e2; }
  .folder-inside__pocket {
    position: absolute; left: 0; bottom: 0; width: 100%; height: 150px; background: var(--pocket);
    clip-path: polygon(0 18%, 60% 18%, 78% 0, 100% 0, 100% 100%, 0 100%);
  }
</style>
</head>
<body>
  <section class="cards-strip">
    <article class="card card--front">
      <h1 class="card__name">Mark Ellis</h1>
      <p class="card__title">Field Supervisor</p>
      <ul class="contact-list">
        <li><span class="dot"></span>855-555-SEAL (Toll Free)</li>
        <li><span class="dot"></span>314-555-0178</li>
        <li><span class="dot"></span>314-555-0142</li>
        <li><span class="dot"></span>800-555-0193</li>
        <li><span class="dot"></span>mellis@slatepeak.example</li>
        <li><span class="dot"></span>www.SlatePeakRestoration.example</li>
        <li class="wrap"><span class="dot"></span><span>2718 Brennan Ave Suite 310 Kirkwood,<br>MO 63122</span></li>
      </ul>
      <div class="card__band">
        <span class="card__license">License #207.538142</span>
        <span class="brand brand--small"><span class="brand__square"></span>Slate Peak</span>
      </div>
    </article>

    <article class="card card--back">
      <div class="brand"><span class="brand__square"></span>Slate Peak Restoration</div>
      <div class="card__statement">
        Residential &amp; Commercial : 314-555-0178<br>
        Accredited Member of the QCA with an A+ Rating
      </div>
      <p class="card__tagline">Dedicated to Being the most Trusted name in the Roofing Industry!</p>
    </article>
  </section>

  <section class="folder-stage">
    <div class="folder-front">
      <div class="brand brand--large"><span class="brand__square"></span>Slate Peak Restoration</div>
      <span class="brand brand--small"><span class="brand__square"></span>Slate Peak</span>
      <div class="folder-front__stripes"><span></span><span></span></div>
    </div>
    <div class="folder-inside">
      <div class="folder-inside__panel"></div>
      <div class="folder-inside__panel"><div class="folder-inside__pocket"></div></div>
    </div>
  </section>
</body>
</html>
```